2 Business Card Designs

Need two business cards designed:
1) for lumora studio (wedding video) website is lumorastudio.com.au
2) for lumora studio (corporate video) website is lumorastudio.net.au

I am looking for something simple, no fancy shapes etc. Just elegant, simple and classy.

Both companies are video companies, one specialising in weddings the other corporate videos. Neither card needs to have any pics of video or camera related images. Please use same colour schemes as respective websites.

Logo is the same but can change colour.

Industry/Entity Type

Camera

Requirements
Must have
• Logo should be either all white or a colour to match websites
Should not have
• swirls, flowers, shapes, etc.

```html
<!DOCTYPE html>
<html lang="en">
<head>
<meta charset="utf-8">
<title>Lumora Studio – Business Cards</title>
<link href="https://fonts.googleapis.com/css2?family=Exo+2:wght@300;400&display=swap" rel="stylesheet">
<style>
  :root {
    --backdrop: #e9e6e1;
    --paper-white: #ffffff;
    --paper-sage: #dfe2cc;
    --card-charcoal: #231f20;
    --card-olive: #686b5c;
    --ink-dark: #231f20;
    --ink-olive: #6b6e5e;
    --ink-light: #ffffff;
    --ink-soft: #d9d9d4;
  }
  * { margin: 0; padding: 0; box-sizing: border-box; }
  html, body {
    width: 1200px; height: 900px; overflow: hidden;
    background: var(--backdrop);
    font-family: "Exo 2", sans-serif;
  }
  .sheet { position: relative; width: 1200px; height: 900px; }

  .card {
    position: absolute; width: 526px; height: 298px; overflow: hidden;
    box-shadow: 0 2px 6px rgba(0,0,0,0.18);
  }
  .card--front-white { left: 43px; top: 136px; background: var(--paper-white); color: var(--ink-dark); }
  .card--back-charcoal { left: 634px; top: 136px; background: var(--card-charcoal); color: var(--ink-light); }
  .card--front-sage { left: 43px; top: 466px; background: var(--paper-sage); color: var(--ink-dark); }
  .card--back-olive { left: 634px; top: 466px; background: var(--card-olive); color: var(--ink-light); }

  .holder-name {
    position: absolute; left: 30px; top: 194px;
    font-size: 24px; font-weight: 400; letter-spacing: 0.2px;
  }
  .holder-contact {
    position: absolute; left: 30px; top: 246px;
    font-size: 11.5px; line-height: 16px; font-weight: 400;
  }
  .front-wordmark {
    position: absolute; left: 262px; top: 196px; width: 244px;
    text-align: center; font-size: 38px; font-weight: 300; letter-spacing: 0.5px;
  }
  .card--front-white .front-wordmark { color: var(--ink-dark); }
  .card--front-sage .front-wordmark { color: var(--ink-olive); }

  .footer-band {
    position: absolute; left: 239px; right: 0; bottom: 0; height: 11px;
  }
  .card--front-white .footer-band { background: var(--card-charcoal); }
  .card--front-sage .footer-band { background: var(--card-olive); }

  .back-wordmark {
    position: absolute; left: 0; right: 0; top: 112px;
    text-align: center; font-size: 44px; font-weight: 300; color: var(--ink-light);
  }
  .back-hours {
    position: absolute; left: 0; right: 0; top: 186px;
    text-align: center; font-size: 13.5px; line-height: 18px; color: var(--ink-light);
  }
  .back-web {
    position: absolute; left: 0; right: 0; top: 260px;
    text-align: center; font-size: 15px; font-weight: 300; letter-spacing: 0.6px; color: var(--ink-soft);
  }
</style>
</head>
<body>
<main class="sheet">
  <section class="card card--front-white">
    <p class="holder-name">Daniel Reyes</p>
    <p class="holder-contact">Marlow :: NSW :: 2075<br>Phone: +61 2 9000 4182</p>
    <p class="front-wordmark">lumora studio</p>
    <div class="footer-band"></div>
  </section>

  <section class="card card--back-charcoal">
    <p class="back-wordmark">lumora studio</p>
    <p class="back-hours">Monday-Friday 9am-5pm<br>Evening Viewings available<br>All bookings via appointment only.212 Harbour Road</p>
    <p class="back-web">www.LumoraStudio.com.au</p>
  </section>

  <section class="card card--front-sage">
    <p class="holder-name">Daniel Reyes</p>
    <p class="holder-contact">Marlow :: NSW :: 2075<br>Phone: +61 2 9000 4182</p>
    <p class="front-wordmark">lumora studio</p>
    <div class="footer-band"></div>
  </section>

  <section class="card card--back-olive">
    <p class="back-wordmark">lumora studio</p>
    <p class="back-hours">Monday-Friday 9am-5pm<br>Evening Viewings available<br>All bookings via appointment only.212 Harbour Road</p>
    <p class="back-web">www.LumoraStudio.com.au</p>
  </section>
</main>
</body>
</html>
```